Website Online Research Solutions

We are a small European high-tech online research company.
With our own state of the art software we run online panels and are conducting reseach for companies. Partly research via our own panel and partly via panels we maintain for our customers.
Our current website is old and outdatet: www.pravelo.nl.
We are in the process to change the content of the site. We want a modern, european and businesslike design for our new website.
Our logo has to stay the same (left uppersite of our website and attached) but can be changed a little to adapt it to the new design of the website. The colors of the site are up to you.
Target Market(s)
Marketeers and researchers of large and middle size companies in all kind of fields.
Industry/Entity Type
Online
Look and feel
Each slider illustrates characteristics of the customer's brand and the style your logo design should communicate.

```html
<!DOCTYPE html>
<html lang="nl">
<head>
<meta charset="utf-8">
<title>Pravelo – Online Research Solutions</title>
<link href="https://fonts.googleapis.com/css2?family=Arimo:wght@400;700&family=Noto+Sans:wght@400;700&display=swap" rel="stylesheet">
<style>
:root{
  --topbar:#1c2a3c;
  --blue-header:#0d4a93;
  --blue-text:#0b4a7e;
  --panel:#d4e1e8;
  --nav-active:#2a5877;
  --ink:#222;
  --white:#fff;
  --footer:#061a35;
  --line:#e4e4e4;
}
*{margin:0;padding:0;box-sizing:border-box}
html,body{width:1200px;height:971px;overflow:hidden;background:var(--white)}
body{position:relative;font-family:"Arimo",Arial,sans-serif;color:var(--ink)}
.abs{position:absolute}
.topbar{left:0;top:0;width:1200px;height:31px;background:linear-gradient(#26364a,var(--topbar));border-bottom:1px solid #4a6486}
.toplinks a,.footlinks a{position:absolute;color:#e8eef5;font-size:11px;text-decoration:none}
.search{left:808px;top:9px;width:148px;height:16px;background:#fff;border:1px solid #aab;font-size:10px;color:#888;padding:2px 8px}
.search-icon{left:962px;top:9px}
.hero-band{left:0;top:31px;width:1200px;height:331px;background:radial-gradient(ellipse 200px 120px at 260px 80px,#2c66ad,transparent),linear-gradient(90deg,#0b3f86,#0f4e9c 50%,#0b418a)}
.hero-band-map{left:0;top:31px;width:1200px;height:331px;background:radial-gradient(ellipse 600px 150px at 700px 120px,rgba(120,160,220,.18),transparent)}
.under-band{left:0;top:362px;width:1200px;height:50px;background:linear-gradient(#dcdcdc,#fff)}
.brand{left:197px;top:51px;width:118px;height:118px;border-radius:50%;background:radial-gradient(circle,#fafafa,#dde2e8);display:flex;align-items:center;justify-content:center;font-family:"Noto Sans",sans-serif;font-weight:700;font-size:21px;color:#1d2e44}
.stage{left:173px;top:177px;width:844px;height:308px;border-radius:6px;background:linear-gradient(#5a8aa9,#7ea3ba 15%,var(--panel) 80%,#e3ebef);box-shadow:2px 3px 4px rgba(0,0,0,.35)}
.nav{left:360px;top:177px;height:34px}
.nav a{position:absolute;top:0;height:34px;line-height:34px;color:#fff;font-size:13.5px;text-decoration:none;text-align:center;border-right:1px solid rgba(255,255,255,.12)}
.nav a.active{background:var(--nav-active)}
.photo{left:183px;top:212px;width:822px;height:258px;background:linear-gradient(180deg,#6c6e70,#a98d6c 40%,#8c7761 70%,#4a4642)}
.caption{left:183px;top:390px;width:822px;height:80px;background:rgba(15,15,15,.82);color:#fff}
.caption h2{position:absolute;left:24px;top:12px;font-size:14px;font-weight:700}
.caption p{position:absolute;left:24px;top:33px;width:580px;font-size:9.8px;line-height:10.6px}
.card{border:1px solid var(--line);border-radius:4px;background:linear-gradient(#f2f2f2,#fff 30%)}
.card-head{position:absolute;left:-1px;top:-1px;right:-1px;height:30px;border-radius:4px 4px 0 0;background:linear-gradient(var(--blue-header),#08407f);color:#fff;font-family:"Noto Sans",sans-serif;font-weight:700;font-size:15px;padding:5px 0 0 15px}
.card-head::after{content:"";position:absolute;left:0;right:0;bottom:0;height:4px;background:linear-gradient(90deg,#4b86c3,#8fb2d6,#4b86c3)}
.about{left:174px;top:508px;width:436px;height:306px}
.about .body{position:absolute;left:14px;top:45px;width:405px;font-size:10px;line-height:11.4px}
.about .lead{color:var(--blue-text);font-weight:700;margin-bottom:10px}
.divider{left:628px;top:508px;width:1px;height:306px;background:var(--line)}
.data{left:647px;top:509px;width:368px;height:153px}
.data .body{position:absolute;left:11px;top:44px;width:334px;font-size:9.8px;line-height:11.9px}
.events-title{left:660px;top:676px;font-family:"Noto Sans",sans-serif;font-size:17px;font-weight:400;color:var(--blue-text)}
.events-title b{font-weight:700}
.date{width:47px;height:41px;border-radius:3px;background:linear-gradient(#1a5aa0,#0a3f7c);color:#fff;text-align:center;box-shadow:1px 1px 2px rgba(0,0,0,.4)}
.date .d{display:block;font-size:17px;line-height:20px;padding-top:2px}
.date .m{display:block;font-size:11px}
.event-text{width:225px;font-size:9.8px;line-height:10.6px}
.footer{left:0;top:853px;width:1200px;height:118px;background:linear-gradient(#06142b,var(--footer) 60%,#051025)}
.foot-mark{left:374px;top:852px;width:146px;height:146px;border-radius:50%;background:rgba(120,140,170,.16);display:flex;align-items:center;justify-content:center;font-family:"Noto Sans",sans-serif;font-weight:700;font-size:24px;color:rgba(150,165,190,.35)}
</style>
</head>
<body>
<div class="abs hero-band"></div>
<div class="abs hero-band-map" role="img" aria-label="Faint dotted world map across the header"></div>
<div class="abs under-band"></div>

<header class="abs topbar">
  <nav class="toplinks">
    <a style="left:185px;top:11px">Home</a>
    <a style="left:248px;top:11px">Latest News</a>
    <a style="left:338px;top:11px">Lorem Ipsum</a>
  </nav>
</header>
<div class="abs search">search</div>
<svg class="abs search-icon" width="14" height="16" viewBox="0 0 14 16"><circle cx="8.5" cy="5.5" r="4" fill="none" stroke="#fff" stroke-width="1.6"/><line x1="5.6" y1="8.6" x2="1.5" y2="14" stroke="#fff" stroke-width="2"/></svg>

<div class="abs brand">Pravelo</div>

<section class="abs stage"></section>
<nav class="abs nav">
  <a class="active" style="left:0;width:97px">Algemeen</a>
  <a style="left:97px;width:106px">Producten</a>
  <a style="left:203px;width:87px">Demo´s</a>
  <a style="left:290px;width:80px">Media</a>
  <a style="left:370px;width:104px">Referenties</a>
  <a style="left:474px;width:100px">Personeel</a>
  <a style="left:574px;width:77px;border-right:0">Contact</a>
</nav>
<div class="abs photo" role="img" aria-label="Photo of the research team working at desks with computer screens in an office"></div>
<div class="abs caption">
  <h2>Algemeen</h2>
  <p>Lorem ipsum dolor sit amet, consectetur adipiscing elit. Phasellus mauris magna, mollis ut dictum eget, viverra in ante. Sed turpis ipsum, lacinia vitae egestas vel, pulvinar sed orci. Praesent ornare nibh id urna tincidunt ut congue ligula dignissim. Mauris lorem nibh, condimentum ut rutrum ut, faucibus vel urna</p>
</div>

<section class="abs card about">
  <h3 class="card-head">Pravelo</h3>
  <div class="body">
    <p class="lead">Pravelo is gespecialiseerd in online gegevensverzameling en analyse en is werkzaam voor internationale opdrachtgevers.</p>
    <p>Het bedrijf werd opgericht in 1998 en is gevestigd in Havelveen, een kleine havenplaats aan de noordkust. Onze produkten zijn ontwikkeld op basis van Kwadra, een krachtige en uitermate flexibele onderzoekstool voor het verzamelen &amp; verwerken van (online) researchgegevens. Kwadra werd ontwikkeld dóór opinieonderzoekers vóór opinieonderzoekers.<br>Ons team bestaat uit zowel opinieonderzoekers als programmeurs met vele jaren ervaring op het gebied van opinieonderzoek en met name met online toepassingen daarvoor.</p>
    <p style="margin-top:11px">Deze bekende sites zijn ontwikkeld en worden beheerd door Pravelo BV:<br>www.meetlint.nl<br>www.schaduwhal.nl<br>www.jongmeter.nl<br>Korvel klantenpanel</p>
  </div>
</section>

<div class="abs divider"></div>

<section class="abs card data">
  <h3 class="card-head">Dataverzameling</h3>
  <p class="body">Pravelo is uitgegroeid tot een volwaardig speler in de markt met een indrukwekkend(e) portfolio. Zo heeft Pravelo sinds haar oprichting wereldwijd meer dan 2.000.000 vragenlijsten afgenomen in diverse talen en voor diverse opdrachtgevers. Onze dienstverlening beperkt zich tot het verzamelen van data, Pravelo trekt geen conclusies maar stelt haar klanten middels ons online analyse product Kwadra Tables in staat zelf conclusies en/of rapportages te maken zodat beslissingen kunnen worden genomen op basis van eigen waarnemingen.</p>
</section>

<h3 class="abs events-title">Recent <b>Events</b></h3>
<div class="abs date" style="left:659px;top:707px"><span class="d">8</span><span class="m">april</span></div>
<p class="abs event-text" style="left:717px;top:711px">Lorem ipsum dolor sit amet, consectetur adipiscing elit. Phasellus mauris magna, mollis ut dictum eget, viverra in ante.</p>
<div class="abs date" style="left:659px;top:768px"><span class="d">8</span><span class="m">april</span></div>
<p class="abs event-text" style="left:717px;top:774px">Lorem ipsum dolor sit amet, consectetur adipiscing elit. Phasellus mauris magna, mollis ut dictum eget, viverra in ante.</p>

<footer class="abs footer"></footer>
<div class="abs foot-mark">Pravelo</div>
<nav class="footlinks">
  <a style="left:530px;top:863px">Home</a>
  <a style="left:593px;top:863px">Latest News</a>
  <a style="left:683px;top:863px">Lorem Ipsum</a>
</nav>
</body>
</html>
```